Marnie Vale Photography needs a unique, creative business card/logo design

I need a design for business cards/logo that is unique and creative in the industry. Simplicity is nice, so not too crowded. Something that will catch my customer's eye and remain in their memory. I am primarily a landscape photographer but will be soon may be branching into boudoir photography as well. I have attached my current card.

Marnie Vale Photography
Phone: 0439 517 264
Email: MarnieValePhotography@quillmail.example
Website: www.snapnook.example/MarnieValePhotography.Aust

Marnie Vale Photography

• Contact Details on one side
• pixelation

```html
<!DOCTYPE html>
<html lang="en">
<head>
<meta charset="utf-8">
<title>Marnie Vale Photography — Business Card</title>
<link href="https://fonts.googleapis.com/css2?family=Roboto:wght@300;400;500&display=swap" rel="stylesheet">
<style>
  :root {
    --page: #e9e6e1;
    --card-top: #1a1e23;
    --card-bottom: #0e1013;
    --card-band: #181b20;
    --accent: #1fa9d8;
    --text-light: #e6eaee;
    --text-muted: #b9c0c7;
  }
  * { box-sizing: border-box; margin: 0; padding: 0; }
  html, body {
    width: 1200px; height: 1023px; overflow: hidden;
    background: var(--page);
    font-family: "Roboto", Arial, sans-serif;
  }
  .sheet {
    position: relative; width: 1200px; height: 1023px;
  }
  .card {
    position: absolute; left: 250px;
    width: 700px; height: 400px;
    border-radius: 22px;
    background: linear-gradient(160deg, var(--card-top), var(--card-bottom));
    box-shadow: 0 10px 30px rgba(0,0,0,.25);
    overflow: hidden;
  }
  .card--contact { top: 70px; }
  .card--brand { top: 553px; }

  /* Contact side */
  .brand-mark {
    position: absolute; right: 46px; top: 44px;
    display: flex; align-items: center; gap: 14px;
  }
  .brand-mark__dot {
    width: 46px; height: 46px; border-radius: 50%;
    background: var(--accent);
  }
  .brand-mark__name {
    color: var(--accent); font-weight: 400; font-size: 17px;
    letter-spacing: 2px; text-transform: uppercase;
  }
  .person {
    position: absolute; left: 54px; top: 128px;
    color: var(--accent); font-weight: 500; font-size: 40px;
  }
  .person-rule {
    position: absolute; left: 54px; top: 186px;
    width: 330px; height: 1px;
    background: linear-gradient(90deg, var(--accent), rgba(31,169,216,0));
  }
  .contact-list {
    position: absolute; left: 58px; top: 214px;
    list-style: none;
  }
  .contact-list li {
    display: flex; align-items: center; gap: 14px;
    color: var(--text-light); font-size: 17px; font-weight: 400;
    margin-bottom: 18px;
  }
  .contact-list svg { width: 18px; height: 18px; flex: none; }
  .web-band {
    position: absolute; left: 0; bottom: 0; width: 100%; height: 62px;
    background: var(--card-band);
    border-top: 1px solid rgba(255,255,255,.04);
    display: flex; align-items: center; padding-left: 58px;
    color: var(--text-light); font-size: 16px; letter-spacing: .3px;
  }

  /* Brand side */
  .brand-stack {
    position: absolute; inset: 0;
    display: flex; flex-direction: column; align-items: center; justify-content: center;
    gap: 28px;
  }
  .brand-stack__dot {
    width: 110px; height: 110px; border-radius: 50%;
    background: var(--accent);
  }
  .brand-stack__name {
    color: var(--text-light); font-weight: 300; font-size: 28px;
    letter-spacing: 12px; text-transform: uppercase; text-align: center;
    line-height: 1.45; padding-left: 12px;
  }
</style>
</head>
<body>
<main class="sheet">

  <section class="card card--contact" aria-label="Contact side">
    <div class="brand-mark">
      <span class="brand-mark__dot"></span>
      <span class="brand-mark__name">Marnie Vale Photography</span>
    </div>

    <h1 class="person">Marnie Holloway</h1>
    <div class="person-rule"></div>

    <ul class="contact-list">
      <li>
        <svg viewBox="0 0 24 24" aria-hidden="true"><path fill="#1fa9d8" d="M6.6 10.8c1.4 2.8 3.8 5.1 6.6 6.6l2.2-2.2c.3-.3.7-.4 1-.2 1.1.4 2.3.6 3.6.6.6 0 1 .4 1 1V20c0 .6-.4 1-1 1C10.6 21 3 13.4 3 4c0-.6.4-1 1-1h3.5c.6 0 1 .4 1 1 0 1.3.2 2.5.6 3.6.1.3 0 .7-.2 1z"/></svg>
        <span>0439 517 264</span>
      </li>
      <li>
        <svg viewBox="0 0 24 24" aria-hidden="true"><rect x="2.5" y="5" width="19" height="14" fill="none" stroke="#1fa9d8" stroke-width="1.6"/><path d="M2.5 5l9.5 8 9.5-8M2.5 19l7-6.5M21.5 19l-7-6.5" fill="none" stroke="#1fa9d8" stroke-width="1.6"/></svg>
        <span>MarnieValePhotography@quillmail.example</span>
      </li>
    </ul>

    <div class="web-band">www.snapnook.example/MarnieValePhotography.Aust</div>
  </section>

  <section class="card card--brand" aria-label="Brand side">
    <div class="brand-stack">
      <span class="brand-stack__dot"></span>
      <p class="brand-stack__name">Marnie Vale<br>Photography</p>
    </div>
  </section>

</main>
</body>
</html>
```